"Pay it Forward" stated in center, with circle design using 5 Icon photo and names.

Graphic Art Image :
Circle flow design of Pay It Forward example files enclosed.
Make graphic art design like ENCLOSED Center of Circle flow: "Pay it Forward Circle"
But with Circle flow of names/ icon's in hand written design ENCLOSED
Use the ENCLOSED Icon's for Business, School, Families, Communities, Dovrik Club
Try to use our green in ENCLSOED Logo Colors in your design---
Target Market(s)
Local Businesses, Schools
Industry/Entity Type
Fund Raising
Font styles to use
Sans Serif
Colors
00AB8E
00BBA5
67D7C9
C6EFE9
E9F9F6
Requirements
Must have
- Circle of Life type design

```html
<!DOCTYPE html>
<html lang="en">
<head>
<meta charset="utf-8">
<title>Pay It Forward</title>
<link rel="stylesheet" href="https://fonts.googleapis.com/css2?family=Archivo:wght@500;700;900&display=swap">
<style>
  :root {
    --backdrop: #b8b8b8;
    --paper: #ffffff;
    --ink: #1f1f1f;
    --green: #2a9544;
    --green-soft: #c6efe9;
    --family-tone-a: #7cae52;
    --family-tone-b: #2f6fa0;
    --shop-tone-a: #f2a35c;
    --shop-tone-b: #8fc1d9;
    --school-tone-a: #f7c046;
    --school-tone-b: #dfe8ea;
    --town-tone-a: #8cbfa0;
    --town-tone-b: #d9a46a;
  }
  html, body {
    margin: 0;
    width: 1200px;
    height: 1200px;
    overflow: hidden;
    background: var(--backdrop);
  }
  .flyer {
    position: absolute;
    left: 236px;
    top: 90px;
    width: 728px;
    height: 1020px;
    display: block;
  }
  .label {
    font-family: "Archivo", Arial, sans-serif;
    font-weight: 500;
    font-size: 27px;
    fill: var(--ink);
    text-anchor: middle;
  }
  .headline-top {
    font-family: "Archivo", Arial, sans-serif;
    font-weight: 700;
    font-size: 78px;
    fill: var(--ink);
    text-anchor: middle;
  }
  .headline-main {
    font-family: "Archivo", Arial, sans-serif;
    font-weight: 900;
    font-size: 128px;
    fill: var(--green);
    stroke: var(--ink);
    stroke-width: 2;
    paint-order: stroke;
    text-anchor: middle;
    letter-spacing: -2px;
  }
  .club-name {
    font-family: "Archivo", Arial, sans-serif;
    font-weight: 700;
    font-size: 40px;
    fill: var(--ink);
    text-anchor: middle;
  }
  .flow-line { fill: none; stroke: var(--ink); stroke-width: 11; stroke-linecap: round; }
  .flow-arrow { fill: none; stroke: var(--green); stroke-width: 24; stroke-linecap: round; }
  .flow-head { fill: var(--green); }
</style>
</head>
<body>
<svg class="flyer" viewBox="380 145 1172 1643" xmlns="http://www.w3.org/2000/svg">
  <defs>
    <linearGradient id="family-fill" x1="0" y1="0" x2="1" y2="1">
      <stop offset="0" stop-color="var(--family-tone-a)"/>
      <stop offset="1" stop-color="var(--family-tone-b)"/>
    </linearGradient>
    <linearGradient id="shop-fill" x1="0" y1="0" x2="0" y2="1">
      <stop offset="0" stop-color="var(--shop-tone-a)"/>
      <stop offset="1" stop-color="var(--shop-tone-b)"/>
    </linearGradient>
    <linearGradient id="school-fill" x1="0" y1="0" x2="0" y2="1">
      <stop offset="0" stop-color="var(--school-tone-a)"/>
      <stop offset="1" stop-color="var(--school-tone-b)"/>
    </linearGradient>
    <radialGradient id="town-fill">
      <stop offset="0" stop-color="var(--town-tone-a)"/>
      <stop offset="1" stop-color="var(--town-tone-b)"/>
    </radialGradient>
  </defs>

  <!-- paper -->
  <rect class="paper" x="380" y="145" width="1172" height="1643" fill="var(--paper)"/>

  <!-- top corner bands -->
  <polygon class="band-dark" points="380,145 1552,145 1552,232 1340,168 380,380" fill="var(--ink)"/>
  <polygon class="band-green" points="380,380 1340,168 1552,232 1552,246 1340,185 380,460" fill="var(--green)"/>
  <polygon class="band-rule" points="380,460 1340,185 1552,246 1340,203 380,466" fill="var(--ink)" opacity="0.15"/>

  <!-- bottom corner bands -->
  <polygon class="band-dark" points="380,1788 1552,1788 1552,1552 590,1762 380,1705" fill="var(--ink)"/>
  <polygon class="band-green" points="380,1705 590,1762 1552,1552 1552,1470 590,1730 380,1684" fill="var(--green)"/>
  <polygon class="band-rule" points="380,1684 590,1730 1552,1470 1552,1466 590,1724 380,1680" fill="var(--ink)" opacity="0.15"/>

  <!-- circular flow lines -->
  <path class="flow-line" d="M1488,780 C1420,560 1200,405 970,405 C720,405 520,560 455,760 C420,870 520,950 600,945 C670,940 705,900 725,860 C780,760 860,695 970,695 C1080,695 1180,770 1228,865"/>
  <path class="flow-line" d="M1228,1070 C1180,1170 1080,1240 970,1240 C860,1240 780,1180 725,1075 C705,1035 670,990 600,990 C520,990 420,1070 455,1190 C520,1400 720,1530 985,1530 C1230,1530 1420,1350 1488,1155"/>

  <!-- direction arrows -->
  <path class="flow-arrow" d="M752,648 Q772,600 830,580"/>
  <polygon class="flow-head" points="823,543 885,567 830,610"/>
  <path class="flow-arrow" d="M1232,645 Q1290,668 1310,715"/>
  <polygon class="flow-head" points="1278,738 1342,708 1326,772"/>
  <path class="flow-arrow" d="M1345,1145 Q1345,1210 1292,1245"/>
  <polygon class="flow-head" points="1244,1262 1308,1266 1282,1205"/>
  <path class="flow-arrow" d="M860,1355 Q792,1360 762,1310"/>
  <polygon class="flow-head" points="733,1266 738,1332 792,1290"/>

  <!-- stations -->
  <rect class="art-families" x="965" y="455" width="170" height="185" rx="16" fill="url(#family-fill)" role="img" aria-label="Illustration of a multi-generation family standing together"/>
  <text class="label" x="1047" y="672">Families</text>

  <rect class="art-vendors" x="515" y="705" width="205" height="150" rx="14" fill="url(#shop-fill)" role="img" aria-label="Illustration of a small open storefront with its owner"/>
  <text class="label" x="613" y="874">Vendors</text>

  <rect class="art-schools" x="1290" y="842" width="185" height="188" rx="16" fill="url(#school-fill)" role="img" aria-label="Icon of a school building"/>
  <text class="label" x="1387" y="1064">Schools</text>

  <circle class="art-communities" cx="1063" cy="1350" r="102" fill="url(#town-fill)" role="img" aria-label="Illustration of a town square with neighbours gathering"/>
  <text class="label" x="1066" y="1476">Communities</text>

  <text class="club-name" x="612" y="1160">Dovrik Club</text>

  <!-- headline -->
  <text class="headline-top" x="985" y="920">Pay It</text>
  <text class="headline-main" x="976" y="1018">Forward</text>
</svg>
</body>
</html>
```